LABEL DESIGN FOR A NATURAL SKIN CARE LINE

We are looking for a label design for a new natural skin care line that targets the mindfulness and yoga community. We offer a everyday face wash that is derived from natural ingredients and combine it with online yoga classes that will match the intention on the back of the product label. Please make the logo prominent on the front of the bottle, play with horizontal and vertical placement. The product is called “Mellow Rinse”. We like a more modern clean feel.

DERMAVOWE is essentially a natural wellness beauty brand that will fuse into a line of products, a design should be versatile and include the colors in the logo along with whites. The final design should communicate a natural feel that will speak to the yoga community and mindfulness movement.

Target Market(s)

Yogis, fitness community, natural products

Industry/Entity Type

Skin Care Product

Font styles to use
Serif
Decorative

Requirements
Must have
• logo on the front that is prominent, with “MELLOW RINSE” as the product name.

Bottle Dimensions:
3OZ 3.35x4.75in (check attachments)
Nice to have
• Unique designs that stand out. Use the colors in logo. Would be great to have a third eye as a watermark
Should not have
• dark colors,

```html
<!DOCTYPE html>
<html lang="en">
<head>
<meta charset="utf-8">
<title>Mellow Rinse Label</title>
<link rel="stylesheet" href="https://fonts.googleapis.com/css2?family=Marcellus&display=swap">
<style>
  :root {
    --page: #ffffff;
    --label: #efefef;
    --silver-light: #f2f2f2;
    --silver-mid: #c9c9c9;
    --silver-dark: #a9a9a9;
    --teal: #1fa89a;
    --green: #8cc63f;
    --ink: #2b2b2b;
    --line: rgba(180, 180, 180, 0.25);
  }
  html, body {
    margin: 0;
    padding: 0;
    width: 900px;
    height: 1200px;
    overflow: hidden;
    background: var(--page);
  }
  .canvas {
    position: relative;
    width: 900px;
    height: 1200px;
  }
  .label {
    position: absolute;
    left: 172px;
    top: 50px;
    width: 556px;
    height: 1100px;
    background: var(--label);
    overflow: hidden;
    font-family: "Marcellus", serif;
  }
  .label-texture {
    position: absolute;
    inset: 420px 0 0 0;
    background:
      radial-gradient(ellipse at 70% 40%, rgba(255,255,255,0.7), transparent 60%),
      linear-gradient(160deg, transparent 30%, var(--line) 50%, transparent 70%);
  }
  .brand-panel {
    position: absolute;
    left: 122px;
    top: 3px;
    width: 314px;
    height: 420px;
    background: linear-gradient(135deg, var(--silver-dark) 0%, var(--silver-light) 50%, var(--silver-mid) 100%);
    display: flex;
    align-items: center;
    justify-content: center;
    gap: 12px;
  }
  .brand-dot {
    width: 18px;
    height: 18px;
    border-radius: 50%;
    background: var(--teal);
    flex: none;
  }
  .brand-name {
    font-size: 34px;
    letter-spacing: 1px;
    color: var(--teal);
    white-space: nowrap;
  }
  .product-name {
    position: absolute;
    left: 44px;
    top: 520px;
    margin: 0;
    font-weight: 400;
    font-size: 92px;
    line-height: 98px;
    letter-spacing: 3px;
  }
  .product-name .line-one { display: block; color: var(--teal); }
  .product-name .line-two { display: block; color: var(--green); }
  .category {
    position: absolute;
    left: 0;
    width: 100%;
    top: 922px;
    text-align: center;
    font-size: 40px;
    color: var(--ink);
  }
  .volume {
    position: absolute;
    left: 147px;
    top: 1002px;
    width: 265px;
    height: 98px;
    line-height: 98px;
    text-align: center;
    font-size: 43px;
    color: var(--ink);
    background: linear-gradient(90deg, var(--silver-dark), var(--silver-light) 50%, var(--silver-dark));
  }
</style>
</head>
<body>
  <div class="canvas">
    <div class="label">
      <div class="label-texture" role="img" aria-label="Faint flowing line pattern across the label"></div>
      <div class="brand-panel">
        <span class="brand-dot"></span>
        <span class="brand-name">DERMAVOWE</span>
      </div>
      <h1 class="product-name">
        <span class="line-one">MELLOW</span>
        <span class="line-two">RINSE</span>
      </h1>
      <div class="category">Natural Skin Care</div>
      <div class="volume">100 ml</div>
    </div>
  </div>
</body>
</html>
```